Property Developer - Simple yet Sophisticated and Sharp Business Card

We are a medium sized property developer involved mainly in townhouse developments and land subdivisions.

The company is looking for a simple, sharp and sophisticated business card that will be given to contractors, land owners, financiers etc and thus will need to look professional.

Property development related graphics and art can be used, however the card is not to be too "busy" or crowded. Our company name is KL Estates which could possibly be incorporated into the graphics or artwork.

Single sided and/or double sided designs will be acceptable.

A Simple, Sophisticated, Sharp design please!

Good Luck !

```html
<!DOCTYPE html>
<html lang="en">
<head>
<meta charset="utf-8">
<title>KL Estates – Business Card</title>
<link href="https://fonts.googleapis.com/css2?family=Overlock:wght@400;700&display=swap" rel="stylesheet">
<style>
  :root {
    --page: #ffffff;
    --edge: #9a9a9a;
    --ink: #1a1a1a;
    --dark-1: #0d0d0d;
    --dark-2: #8a8a8a;
    --green: #6fdc00;
    --lime: #b6f200;
    --glow: #f6ff5a;
    --rim: #ffffff;
  }
  * { margin: 0; padding: 0; box-sizing: border-box; }
  html, body {
    width: 886px; height: 1200px; overflow: hidden;
    background: var(--page);
  }
  body { position: relative; font-family: "Overlock", "Trebuchet MS", sans-serif; color: var(--ink); }
  .card {
    position: absolute; left: 0; width: 886px; height: 582px;
    border: 2px solid var(--edge); overflow: hidden;
  }
  .card--front { top: 0; }
  .card--back { top: 618px; }
  .card__art { position: absolute; inset: 0; width: 100%; height: 100%; }
  .card__text { position: absolute; white-space: nowrap; line-height: 1; }
  .right { right: 14px; text-align: right; }
  .center { left: 0; width: 100%; text-align: center; }
  .left { left: 12px; }
  .email { font-size: 21px; }
  .address { font-size: 19px; }
  .company-title { font-size: 84px; }
  .contact { font-size: 29px; font-weight: 700; }
  .company-small { font-size: 27px; }
  .person-name { font-size: 86px; }
  .role { font-size: 35px; }
</style>
</head>
<body>

<section class="card card--front">
  <svg class="card__art" viewBox="0 0 886 582" preserveAspectRatio="none" aria-hidden="true">
    <defs>
      <linearGradient id="darkFront" x1="0" y1="0" x2="1" y2="1">
        <stop offset="0" stop-color="var(--dark-1)"/>
        <stop offset="0.35" stop-color="var(--dark-2)"/>
        <stop offset="0.65" stop-color="var(--dark-2)"/>
        <stop offset="1" stop-color="var(--dark-1)"/>
      </linearGradient>
      <radialGradient id="greenFront" cx="0.5" cy="0.5" r="0.6">
        <stop offset="0" stop-color="var(--glow)"/>
        <stop offset="0.45" stop-color="var(--lime)"/>
        <stop offset="1" stop-color="var(--green)"/>
      </radialGradient>
    </defs>
    <rect width="886" height="582" fill="url(#darkFront)"/>
    <path d="M0,582 L0,464 C71,178 357,36 749,0 L886,0 L886,107 C838,410 588,553 267,582 Z"
          fill="url(#greenFront)" stroke="var(--rim)" stroke-width="5"/>
  </svg>
  <div class="card__text right email" style="top:8px">projects.klestates@mail.com</div>
  <div class="card__text right address" style="top:66px">PO Box 4521 Riverside QLD 4170</div>
  <div class="card__text center company-title" style="top:222px">KL Estates</div>
  <div class="card__text left contact" style="top:476px">Phone: (07) 3200 1840</div>
  <div class="card__text left contact" style="top:526px">Fax: (07) 3200 1841</div>
</section>

<section class="card card--back">
  <svg class="card__art" viewBox="0 0 886 582" preserveAspectRatio="none" aria-hidden="true">
    <defs>
      <linearGradient id="darkBack" x1="0" y1="0" x2="1" y2="1">
        <stop offset="0" stop-color="var(--dark-1)"/>
        <stop offset="0.35" stop-color="var(--dark-2)"/>
        <stop offset="0.65" stop-color="var(--dark-2)"/>
        <stop offset="1" stop-color="var(--dark-1)"/>
      </linearGradient>
      <radialGradient id="greenBack" cx="0.5" cy="0.5" r="0.6">
        <stop offset="0" stop-color="var(--glow)"/>
        <stop offset="0.45" stop-color="var(--lime)"/>
        <stop offset="1" stop-color="var(--green)"/>
      </radialGradient>
    </defs>
    <rect width="886" height="582" fill="url(#darkBack)"/>
    <path d="M0,582 L0,260 C110,110 380,20 680,0 L886,0 L886,95 C850,390 620,545 340,582 Z"
          fill="url(#greenBack)" stroke="var(--rim)" stroke-width="5"/>
  </svg>
  <div class="card__text right email" style="top:28px; font-size:24px">daniel.klestates@mail.com</div>
  <div class="card__text center company-small" style="top:142px">KL Estates</div>
  <div class="card__text center person-name" style="top:218px">Daniel Hart</div>
  <div class="card__text center role" style="top:358px">Advertising Manager</div>
  <div class="card__text left contact" style="top:490px; font-size:27px">Office: (07) 3200 1842</div>
  <div class="card__text left contact" style="top:530px; font-size:27px">Cell: 0412 555 019</div>
</section>

</body>
</html>
```